DJ Marcus Tevane

I'm looking for a professional but still artsy/progressive design. I come from a hip hop/club DJ background playing a lot of underground music but have switched to doing more corporate parties and weddings recently. I am all about keeping the dancefloor moving and emotionally connecting with the crowd. I'd like a trendy/updated color palette. Something that's clean enough that looks professional but also trendy enough to convey that by the end of the night we'll be sweatily dancing to the latest hits. Some designers/artists I like: Rolo Pemberack, Gavin Struthe, Dorian Fellick, Orbitex 3100, Wade Ipsley.

```html
<!DOCTYPE html>
<html lang="en">
<head>
<meta charset="utf-8">
<title>DJ Marcus Tevane — Business Card</title>
<link rel="stylesheet" href="https://fonts.googleapis.com/css2?family=Michroma&family=Open+Sans:wght@400;600&display=swap">
<style>
  :root {
    --backdrop: #222223;
    --card: #f4f4f6;
    --band: #3a3839;
    --ink: #0d0d0d;
    --band-text: #f1f1f1;
    --gold-light: #e6d196;
    --gold-mid: #b8974f;
    --gold-dark: #6a5424;
  }
  * { margin: 0; padding: 0; box-sizing: border-box; }
  html, body {
    width: 1200px;
    height: 800px;
    overflow: hidden;
    background: var(--backdrop);
  }
  .canvas {
    position: relative;
    width: 1200px;
    height: 800px;
  }
  .card {
    position: absolute;
    left: 100px;
    top: 120px;
    width: 1000px;
    height: 560px;
    background: var(--card);
  }
  .identity {
    position: absolute;
    left: 190px;
    top: 196px;
    display: flex;
    align-items: center;
    gap: 36px;
  }
  .identity-mark {
    width: 62px;
    height: 62px;
    background: linear-gradient(135deg, var(--gold-light), var(--gold-mid) 50%, var(--gold-dark));
  }
  .identity-name {
    font-family: "Michroma", sans-serif;
    font-size: 40px;
    font-weight: 400;
    color: var(--ink);
    letter-spacing: -1px;
    white-space: nowrap;
  }
  .contact-band {
    position: absolute;
    left: 0;
    top: 441px;
    width: 1000px;
    height: 88px;
    background: var(--band);
    display: flex;
    align-items: center;
    padding-left: 62px;
  }
  .contact-item {
    display: flex;
    align-items: center;
    gap: 14px;
    font-family: "Open Sans", sans-serif;
    font-size: 14px;
    font-weight: 600;
    line-height: 1.35;
    color: var(--band-text);
  }
  .contact-item.address { width: 218px; }
  .contact-item.email { width: 222px; }
  .contact-item.phone { width: 221px; }
  .contact-icon {
    width: 32px;
    height: 32px;
    flex: none;
  }
</style>
</head>
<body>
<div class="canvas">
  <section class="card">
    <div class="identity">
      <div class="identity-mark"></div>
      <h1 class="identity-name">DJ MARCUS TEVANE</h1>
    </div>

    <svg width="0" height="0" style="position:absolute">
      <defs>
        <linearGradient id="gold" x1="0" y1="0" x2="1" y2="1">
          <stop offset="0" stop-color="#e6d196"/>
          <stop offset="0.5" stop-color="#b8974f"/>
          <stop offset="1" stop-color="#6a5424"/>
        </linearGradient>
      </defs>
    </svg>

    <div class="contact-band">
      <div class="contact-item address">
        <svg class="contact-icon" viewBox="0 0 32 32" aria-hidden="true">
          <circle cx="16" cy="16" r="16" fill="url(#gold)"/>
          <path d="M8 16 L16 9 L24 16 L21.5 16 L21.5 23 L18 23 L18 18.5 L14 18.5 L14 23 L10.5 23 L10.5 16 Z" fill="#f6f1e2"/>
        </svg>
        <span>Street Address Here<br>Singapore, 2222</span>
      </div>
      <div class="contact-item email">
        <svg class="contact-icon" viewBox="0 0 32 32" aria-hidden="true">
          <circle cx="16" cy="16" r="16" fill="url(#gold)"/>
          <path d="M9 9 L24 16 L9 23 L12 16 Z" fill="#3a3839"/>
        </svg>
        <span>bookings@tevanemail.net</span>
      </div>
      <div class="contact-item phone">
        <svg class="contact-icon" viewBox="0 0 32 32" aria-hidden="true">
          <circle cx="16" cy="16" r="16" fill="url(#gold)"/>
          <path d="M9 12 Q16 7 23 12 L21 14.5 L19 13 L13 13 L11 14.5 Z" fill="#3a3839"/>
          <rect x="11" y="15.5" width="10" height="7" rx="1.5" fill="#3a3839"/>
          <circle cx="16" cy="19" r="2" fill="#d9c38a"/>
        </svg>
        <span>+18 2555 0146 3920<br>+18 2555 0146 3920</span>
      </div>
      <div class="contact-item web">
        <svg class="contact-icon" viewBox="0 0 32 32" aria-hidden="true">
          <circle cx="16" cy="16" r="16" fill="url(#gold)"/>
          <circle cx="16" cy="16" r="7" fill="none" stroke="#3a3839" stroke-width="1.6"/>
          <ellipse cx="16" cy="16" rx="3" ry="7" fill="none" stroke="#3a3839" stroke-width="1.4"/>
          <line x1="9" y1="16" x2="23" y2="16" stroke="#3a3839" stroke-width="1.4"/>
        </svg>
        <span>www.tevanesound.net</span>
      </div>
    </div>
  </section>
</div>
</body>
</html>
```